Veltrane Hand Sanitiser Spray Product Range for International Markets

Veltrane is a new Healthcare business launching a full product range of Anti-bacterial Hand Sanitiser Spray bottles in various sizes. We have a new logo which we believe differentiates us from the competition: Veltrane - Care That Goes Further
The Product Range will comprise two distinct product solution types:
- Anti-bacterial Hand Sanitisers - Alcohol based
- Anti-bacterial Hand Sanitisers - Sensitive Non Alcohol based
Bottle sizes will comprise a range containing:
100ml, 250ml, 500ml, 1ltr, 5ltr, 10ltr
Some bottles will have Pump Sprays
The Product labelling will be attractive front packaging label combined with strong product attributes and usage indicator cues.
As a Healthcare brand our logo design is light Green. We believe that this should be combined with blues and greens balanced to create contrast and strong stand-out on-shelf.
A review of competitor brands will show some similar colour cues, however as a Healthcare brand, the colour cues Green and White are synonymous with the sector. Many existing brands are very pragmatic in their label design. i.e. #it does what is says on the tin approach#. Our brand will need strong stand-out and strong aesthetic appeal too, since it will often be left in public view and around the home and office and therefore should look as attractive as possible. There will be other brand variants in the future and thought should be given to this too - with use of colour cues.
For Competitor indicators check-out the brands on Brisklot - Pine Hollow, Dermavell and others....Thank-you!

Target Market(s)

First: Female 25 - 65
Second: Male 25 - 65

Contact Information for Business Card

Garth L. Dunmore
CEO
Veltrane Healthcare Worldwide
'Care That Goes Further'
www.VeltraneHealthcare.example
E. gldunmore@veltranehealthcare.example
T. +44 7700 900318
T. +44 118 496072

Font styles to use
Sans Serif

Colors
34a7d7
33b8a4
add136
fbee3e
b768aa

```html
<!DOCTYPE html>
<html lang="en">
<head>
<meta charset="utf-8">
<title>Veltrane Hand Sanitiser Label – 100ml</title>
<link rel="stylesheet" href="https://fonts.googleapis.com/css2?family=Montserrat:wght@400;500;800&display=swap">
<style>
  :root {
    --brand-green: #44b14a;
    --label-white: #ffffff;
  }
  html, body {
    margin: 0;
    padding: 0;
    width: 800px;
    height: 1200px;
    overflow: hidden;
    background: var(--label-white);
  }
  .label {
    position: relative;
    width: 800px;
    height: 1200px;
    background: var(--label-white);
    font-family: "Montserrat", sans-serif;
    color: var(--brand-green);
  }
  .label-text {
    position: absolute;
    left: 0;
    width: 800px;
    margin: 0;
    text-align: center;
    line-height: 1;
    white-space: nowrap;
  }
  .brand-name {
    top: 188px;
    font-size: 130px;
    font-weight: 500;
    letter-spacing: -2px;
  }
  .brand-tagline {
    top: 327px;
    font-size: 28px;
    font-weight: 400;
    letter-spacing: 6px;
    text-transform: uppercase;
  }
  .product-panel {
    position: absolute;
    left: 27px;
    top: 637px;
    width: 745px;
    height: 466px;
    box-sizing: border-box;
    border: 6px solid var(--brand-green);
  }
  .product-panel-fill {
    position: absolute;
    left: 14px;
    top: 14px;
    right: 14px;
    bottom: 14px;
    background: var(--brand-green);
  }
  .product-claim,
  .product-base {
    font-size: 44px;
    font-weight: 400;
    color: var(--label-white);
  }
  .product-claim { top: 701px; }
  .product-base { top: 1011px; }
  .product-name {
    font-size: 120px;
    font-weight: 800;
    letter-spacing: -4px;
    color: var(--label-white);
  }
  .product-name--first { top: 751px; }
  .product-name--second { top: 876px; }
  .product-volume {
    top: 1123px;
    font-size: 58px;
    font-weight: 800;
    letter-spacing: -1px;
  }
</style>
</head>
<body>
  <main class="label">
    <h1 class="label-text brand-name">Veltrane</h1>
    <p class="label-text brand-tagline">Care That Goes Further</p>

    <div class="product-panel">
      <div class="product-panel-fill"></div>
    </div>
    <p class="label-text product-claim">ANTI-BACTERIAL</p>
    <h2 class="label-text product-name product-name--first">HAND</h2>
    <h2 class="label-text product-name product-name--second">SANITIZER</h2>
    <p class="label-text product-base">ALCOHOL BASED</p>

    <p class="label-text product-volume">100ml</p>
  </main>
</body>
</html>
```